Salon and Spa Distributor Business Card

Need a business card. We are are distributor in the salon and spa industry. We identify with natural beauty. Need a card with:
Company Name: Petal Haven"
Title: "President & CEO"
Address
Company Phone number
email
website
Tag Line:" Pure Care for Every Studio"

Industry/Entity Type

Business

Contact Information for Business Card

Name: Lena Morcott
Title: "President & CEO"
Address: 317 Birchfield Ln, Oakvane, NJ 07481
Company Phone number: 800-463-9152
email: lenamorcott@petalhaven-example.com
website: www.petalhaven-example.com

Requirements
Should not have
• No black backgrounds

```html
<!DOCTYPE html>
<html lang="en">
<head>
<meta charset="utf-8">
<title>Petal Haven — Business Card</title>
<link href="https://fonts.googleapis.com/css2?family=Quicksand:wght@400;500;600;700&display=swap" rel="stylesheet">
<style>
  :root {
    --page: #ecebe8;
    --olive: #6f8e3a;
    --olive-deep: #5f7d30;
    --lime: #9cc21b;
    --leaf: #1f9a45;
    --ink: #2c2f38;
    --paper: #ffffff;
    --text: #3a3d44;
    --muted: #6a6d73;
  }
  * { margin: 0; padding: 0; box-sizing: border-box; }
  html, body { width: 1200px; height: 900px; overflow: hidden; }
  body {
    background: var(--page);
    font-family: "Quicksand", sans-serif;
    color: var(--text);
    position: relative;
  }
  .card {
    position: absolute;
    top: 300px;
    width: 525px;
    height: 300px;
    background: var(--paper);
    overflow: hidden;
    box-shadow: 0 6px 18px rgba(0,0,0,0.12);
  }
  .card--front { left: 55px; }
  .card--back { left: 620px; }
  .card__art { position: absolute; inset: 0; width: 525px; height: 300px; }

  /* front */
  .front-brand {
    position: absolute; left: 75px; top: 60px;
    display: flex; align-items: center; gap: 20px;
  }
  .brand-dot {
    width: 62px; height: 62px; border-radius: 50%;
    background: rgba(255,255,255,0.88);
    flex: none;
  }
  .front-brand__name {
    font-size: 32px; font-weight: 500; color: var(--paper); line-height: 1;
  }
  .front-brand__tag {
    font-size: 14px; font-weight: 500; color: var(--paper); margin-top: 8px;
  }
  .front-web {
    position: absolute; left: 0; right: 0; top: 222px;
    display: flex; justify-content: center; align-items: center; gap: 6px;
    font-size: 13px; font-weight: 500; color: var(--text);
  }

  /* back */
  .back-brand {
    position: absolute; left: 0; width: 235px; top: 60px;
    display: flex; flex-direction: column; align-items: center;
  }
  .back-brand .brand-dot { width: 84px; height: 84px; }
  .back-brand__name {
    font-size: 23px; font-weight: 500; color: var(--paper); margin-top: 28px; line-height: 1;
  }
  .back-brand__tag {
    font-size: 10.5px; font-weight: 500; color: var(--paper); margin-top: 7px;
  }
  .person { position: absolute; left: 300px; top: 38px; }
  .person__name { font-size: 20px; font-weight: 700; color: var(--ink); line-height: 1.1; }
  .person__title { font-size: 10.5px; font-weight: 500; color: var(--muted); margin-top: 2px; }
  .person__rule { width: 64px; height: 3px; background: var(--lime); margin-top: 5px; }
  .contact-icons { position: absolute; left: 296px; top: 95px; }
  .contact {
    position: absolute; left: 326px;
    font-size: 10px; font-weight: 500; color: var(--text); line-height: 1.35;
  }
  .contact--phone { top: 103px; }
  .contact--web { top: 144px; }
  .contact--address { top: 192px; }
</style>
</head>
<body>

<section class="card card--front" aria-label="Business card front">
  <svg class="card__art" viewBox="0 0 525 300" aria-hidden="true">
    <path d="M0 0H525V72C430 152 262 186 0 178Z" fill="var(--lime)"/>
    <path d="M0 0H525V42C420 122 250 152 0 146Z" fill="var(--olive)"/>
    <path d="M0 0H525V20C400 60 200 45 0 70Z" fill="var(--olive-deep)" opacity="0.5"/>
    <path d="M0 184C262 194 432 158 525 78V300H0Z" fill="var(--paper)"/>
    <path d="M0 184L0 252L58 196Z" fill="var(--leaf)"/>
    <path d="M0 184C262 194 432 158 525 78" fill="none" stroke="var(--ink)" stroke-width="7"/>
  </svg>
  <div class="front-brand">
    <span class="brand-dot"></span>
    <div>
      <div class="front-brand__name">Petal Haven</div>
      <div class="front-brand__tag">Pure Care for Every Studio</div>
    </div>
  </div>
  <div class="front-web">
    <svg width="11" height="11" viewBox="0 0 12 12" aria-hidden="true">
      <circle cx="6" cy="6" r="5" fill="none" stroke="var(--text)" stroke-width="1.2"/>
      <ellipse cx="6" cy="6" rx="2.2" ry="5" fill="none" stroke="var(--text)" stroke-width="1"/>
      <line x1="1" y1="6" x2="11" y2="6" stroke="var(--text)" stroke-width="1"/>
    </svg>
    <span>www.petalhaven-example.com</span>
  </div>
</section>

<section class="card card--back" aria-label="Business card back">
  <svg class="card__art" viewBox="0 0 525 300" aria-hidden="true">
    <path d="M250 0H330L270 46Z" fill="var(--leaf)"/>
    <path d="M215 300L290 300L240 250Z" fill="var(--leaf)"/>
    <path d="M0 0H238C292 90 292 210 230 300H0Z" fill="var(--ink)"/>
    <path d="M0 0H230C282 90 282 210 221 300H0Z" fill="var(--lime)"/>
    <path d="M0 0H214C264 90 264 210 205 300H0Z" fill="var(--olive)"/>
    <path d="M0 0H150C200 90 200 210 140 300H0Z" fill="var(--olive-deep)" opacity="0.35"/>
  </svg>
  <div class="back-brand">
    <span class="brand-dot"></span>
    <div class="back-brand__name">Petal Haven</div>
    <div class="back-brand__tag">Pure Care for Every Studio</div>
  </div>

  <div class="person">
    <div class="person__name">Lena Morcott</div>
    <div class="person__title">President &amp; CEO</div>
    <div class="person__rule"></div>
  </div>

  <svg class="contact-icons" width="24" height="120" viewBox="0 0 24 120" aria-hidden="true">
    <line x1="12" y1="16" x2="12" y2="100" stroke="var(--ink)" stroke-width="2"/>
    <circle cx="12" cy="15" r="10" fill="var(--leaf)"/>
    <path d="M7.5 12.5c0-1.5 2-2.5 4.5-2.5s4.5 1 4.5 2.5l-1.8.8-1-1.3h-3.4l-1 1.3Z M8.5 14.5h7l1 4h-9Z" fill="#fff"/>
    <circle cx="12" cy="57" r="10" fill="var(--lime)"/>
    <circle cx="12" cy="57" r="5" fill="none" stroke="#fff" stroke-width="1.3"/>
    <line x1="7" y1="57" x2="17" y2="57" stroke="#fff" stroke-width="1"/>
    <ellipse cx="12" cy="57" rx="2" ry="5" fill="none" stroke="#fff" stroke-width="1"/>
    <circle cx="12" cy="104" r="10" fill="var(--ink)"/>
    <path d="M12 110c-2.5-3-4-5-4-7a4 4 0 0 1 8 0c0 2-1.5 4-4 7Z" fill="#fff"/>
    <circle cx="12" cy="103" r="1.5" fill="var(--ink)"/>
  </svg>

  <div class="contact contact--phone">800-463-9152</div>
  <div class="contact contact--web">www.petalhaven-example.com<br>lenamorcott@petalhaven-example.com</div>
  <div class="contact contact--address">317 Birchfield Ln, Oakvane,<br>NJ 07481</div>
</section>

</body>
</html>
```